Lantern Freightways Advertising Flyers

Our logistical company handles purchasing, receiving, and shipment of goods to the Bahamas and we would like to start our marketing and advertising push. The company will also deliver items to clients as well, similar to an Vexoria type of experience. We already have our logo designed and we would like to setup our advertising look and feel for our flyers and banner ads. I would like design templates for:
Full Page Flyer: 8.5 in. X 11 in. (width x height) in PDF
Social Media 1: 1080 px x 1350 px (width x height) in JPG or PNG
Social Media 2: 1080 px X 1080 px (width x height) in JPG or PNG
I would like all the PSD files and the information for all fonts used within all the designs as well. I'm sharing our logo and font files for incorporating into the design and for branding.
For design references that we like please review the attached folder with design examples for reference.
The call to action on the flyer/banners should be:
Company Address:
517 NE 19th Lane, Ft. Lauderdale, Florida 33308
Email: Lantern817@mailbrook.net
Website: Lantern817.net
We just need them for placeholders and we can add more contact information once the design concepts are confirmed.

Target Market(s)

Persons buying goods online and needing them shipped to them.

Requirements
Must have
• Designs should have strong design elements and be easy to adjust or tweak with copy if necessary.
Nice to have
• I provided examples of designs we like but it doesn't have to be exact.

```html
<!DOCTYPE html>
<html lang="en">
<head>
<meta charset="utf-8">
<title>Lantern Freightways Flyer</title>
<link href="https://fonts.googleapis.com/css2?family=Montserrat:wght@600;700;800&family=Lato:wght@400;700&display=swap" rel="stylesheet">
<style>
  :root {
    --navy: #24205e;
    --purple: #5a58b4;
    --purple-soft: #6b68c4;
    --green: #7ab83a;
    --white: #ffffff;
    --page: #d6d6d6;
  }
  html, body { margin: 0; padding: 0; overflow: hidden; }
  body {
    width: 1200px; height: 1181px;
    background: var(--page);
    position: relative;
    font-family: "Lato", sans-serif;
  }
  .flyer {
    position: absolute; left: 175px; top: 40px;
    width: 850px; height: 1100px;
    background: var(--navy);
    overflow: hidden;
    box-shadow: 0 10px 30px rgba(0,0,0,.25);
    color: var(--white);
  }
  .flyer-art { position: absolute; inset: 0; }
  .brand {
    position: absolute; right: 70px; top: 450px;
    display: flex; align-items: center; gap: 14px;
  }
  .brand-dot { width: 46px; height: 46px; border-radius: 50%; background: var(--green); }
  .brand-name {
    font-family: "Montserrat", sans-serif; font-weight: 600;
    font-size: 30px; color: var(--white); letter-spacing: .5px;
  }
  .headline {
    position: absolute; right: 70px; top: 540px; margin: 0;
    font-family: "Montserrat", sans-serif; font-weight: 800;
    font-size: 62px; line-height: 1.12; text-align: right;
  }
  .about { position: absolute; left: 60px; top: 690px; width: 560px; }
  .about-title { margin: 0 0 10px; font-family: "Lato", sans-serif; font-weight: 400; font-size: 42px; }
  .about p { margin: 0 0 10px; font-size: 14.5px; line-height: 1.4; }
  .contact-lines { position: absolute; left: 60px; top: 880px; font-size: 16px; }
  .contact-line { display: flex; align-items: center; gap: 12px; margin-bottom: 6px; font-weight: 700; }
  .contact-line svg { width: 24px; height: 24px; }
  .site { margin-top: 14px; font-size: 17px; letter-spacing: .5px; }
  .cta { position: absolute; right: 80px; top: 880px; text-align: right; }
  .cta svg { width: 80px; height: 70px; }
  .cta-label { margin: 6px 0 0; font-family: "Montserrat", sans-serif; font-weight: 600; font-size: 34px; }
  .cta-phone { margin: 0; font-family: "Montserrat", sans-serif; font-weight: 700; font-size: 38px; }
</style>
</head>
<body>
<main class="flyer">
  <svg class="flyer-art" viewBox="0 0 850 1100" width="850" height="1100">
    <defs>
      <linearGradient id="sunset" x1="0" y1="0" x2="0" y2="1">
        <stop offset="0" stop-color="#e9a462"/>
        <stop offset=".45" stop-color="#c98a6a"/>
        <stop offset="1" stop-color="#4a5060"/>
      </linearGradient>
      <linearGradient id="yard" x1="0" y1="0" x2="1" y2="1">
        <stop offset="0" stop-color="#c9d8e6"/>
        <stop offset=".5" stop-color="#b86a4e"/>
        <stop offset="1" stop-color="#5f8a9a"/>
      </linearGradient>
    </defs>
    <rect width="850" height="640" fill="url(#sunset)" role="img" aria-label="Photo of a container truck at a port at sunset with a plane overhead"/>
    <path d="M330,700 Q560,360 850,150 L850,230 Q520,420 300,720 Z" fill="var(--purple-soft)" opacity=".75"/>
    <path d="M300,720 Q520,420 850,230 L850,300 Q580,440 320,730 Z" fill="var(--purple)"/>
    <path d="M0,600 L300,720 Q580,440 850,300 L850,1100 L0,1100 Z" fill="var(--navy)"/>
    <circle cx="190" cy="470" r="120" fill="url(#yard)" stroke="var(--white)" stroke-width="8" role="img" aria-label="Photo of stacked shipping containers at a port"/>
    <path d="M300,1100 Q560,880 850,790 L850,1100 Z" fill="var(--green)"/>
  </svg>

  <div class="brand">
    <span class="brand-dot"></span>
    <span class="brand-name">Lantern Freightways</span>
  </div>

  <h1 class="headline">Lorem<br>ipsum dolor<br>sit amet</h1>

  <section class="about">
    <h2 class="about-title">About Us</h2>
    <p>Lorem ipsum dolor sit amet, consectetuer adipiscing elit, sed diam nonummy nibh euismod tincidunt ut laoreet dolore magna aliquam erat volutpat. Ut wisi enim ad minim veniam. Lorem ipsum dolor sit amet.</p>
    <p>Ut nam quas decore maiorum, has te solet affert, ius cu meis quaerendum. Tota possit animal mei te, et nec illud fabellas interpretaris.</p>
  </section>

  <section class="contact-lines">
    <div class="contact-line">
      <svg viewBox="0 0 24 24" fill="none" stroke="#fff" stroke-width="1.6"><path d="M12 22s7-7 7-12a7 7 0 0 0-14 0c0 5 7 12 7 12z"/><circle cx="12" cy="10" r="2.5"/></svg>
      <span>Your first address line</span>
    </div>
    <div class="contact-line">
      <svg viewBox="0 0 24 24" fill="none" stroke="#fff" stroke-width="1.6"><circle cx="12" cy="12" r="9"/><path d="M3 12h18M12 3c3 3 3 15 0 18M12 3c-3 3-3 15 0 18"/></svg>
      <span>Your second address line</span>
    </div>
    <div class="site">COMPANYNAME.COM</div>
  </section>

  <section class="cta">
    <svg viewBox="0 0 80 70" fill="none" stroke="#fff" stroke-width="3" stroke-linejoin="round">
      <path d="M10 50 Q5 40 18 36 L26 44 Q40 36 50 22 L42 14 Q46 2 56 6 Q70 14 62 32 Q50 56 24 62 Q14 62 10 50 Z"/>
    </svg>
    <p class="cta-label">Contact Us</p>
    <p class="cta-phone">012 - 345-6789</p>
  </section>
</main>
</body>
</html>
```